Business Cards for a law firm

Business cards for our law firm. Use our silhoette logo and OAK HARBOR - check our website (www.oakharbor-legal.com)

Contact Information for Business Card

our silhouette logo, OAK HARBOR, 800-555-0147, Dorian Kestrup, dorian@oakharbor-legal.com

Requirements
Must have
• our silhouette logo, OAK HARBOR, 800-555-0147, Dorian Kestrup, dorian@oakharbor-legal.com

```html
<!DOCTYPE html>
<html lang="en">
<head>
<meta charset="utf-8">
<title>Oak Harbor – Business Cards</title>
<link rel="stylesheet" href="https://fonts.googleapis.com/css2?family=Cinzel:wght@500&family=Mulish:wght@300;700&display=swap">
<style>
  :root {
    --page-bg: #e8e8e9;
    --navy: #1f3570;
    --blue-deep: #2b4a8e;
    --blue-light: #3f64a6;
    --card-white: #ffffff;
    --ink: #1c1c1c;
    --ink-soft: #2a2a2a;
  }
  * { margin: 0; padding: 0; box-sizing: border-box; }
  html, body {
    width: 1200px; height: 1200px; overflow: hidden;
    background: var(--page-bg);
  }
  .canvas { position: relative; width: 1200px; height: 1200px; }

  .card { position: absolute; width: 775px; height: 446px; }

  /* Front */
  .card-front { left: 198px; top: 128px; overflow: hidden; }
  .front-backdrop {
    position: absolute; inset: 0;
    background:
      linear-gradient(160deg, rgba(255,255,255,0.08) 0%, rgba(255,255,255,0) 45%),
      linear-gradient(100deg, var(--blue-light) 0%, var(--blue-deep) 55%, #2a4789 100%);
  }
  .front-brand {
    position: absolute; left: 96px; top: 170px;
    display: flex; align-items: center; gap: 30px;
  }
  .brand-dot {
    width: 78px; height: 78px; border-radius: 50%;
    background: var(--card-white);
  }
  .brand-name {
    font-family: "Cinzel", serif; font-weight: 500;
    font-size: 46px; letter-spacing: 4px; line-height: 1;
    color: var(--card-white);
  }

  /* Back */
  .card-back { left: 197px; top: 663px; background: var(--card-white); height: 442px; }
  .back-brand {
    position: absolute; left: 90px; top: 200px; width: 180px;
    font-family: "Cinzel", serif; font-weight: 500;
    font-size: 30px; letter-spacing: 3px; line-height: 1.15;
    color: var(--navy); text-align: center;
  }
  .holder-name {
    position: absolute; left: 346px; top: 118px;
    font-family: "Mulish", sans-serif; font-weight: 700;
    font-size: 22px; color: var(--ink); letter-spacing: 0.3px;
  }
  .contact-list {
    position: absolute; left: 346px; top: 232px; list-style: none;
    font-family: "Mulish", sans-serif; font-weight: 300;
    font-size: 24px; color: var(--ink-soft); line-height: 31px;
  }
  .contact-item { display: flex; align-items: center; gap: 14px; }
  .contact-icon { width: 22px; height: 22px; fill: var(--navy); flex: none; }
</style>
</head>
<body>
<main class="canvas">

  <section class="card card-front" aria-label="Card front">
    <div class="front-backdrop" role="img" aria-label="Upward view of blue glass skyscrapers"></div>
    <div class="front-brand">
      <span class="brand-dot"></span>
      <span class="brand-name">OAK HARBOR</span>
    </div>
  </section>

  <section class="card card-back" aria-label="Card back">
    <div class="back-brand">OAK HARBOR</div>
    <p class="holder-name">Dorian Kestrup</p>
    <ul class="contact-list">
      <li class="contact-item">
        <svg class="contact-icon" viewBox="0 0 24 24" aria-hidden="true"><path d="M6.6 10.8c1.4 2.8 3.8 5.1 6.6 6.6l2.2-2.2c.3-.3.7-.4 1-.2 1.1.4 2.3.6 3.6.6.6 0 1 .4 1 1V20c0 .6-.4 1-1 1C10.6 21 3 13.4 3 4c0-.6.4-1 1-1h3.5c.6 0 1 .4 1 1 0 1.3.2 2.5.6 3.6.1.3 0 .7-.2 1z"/></svg>
        <span>800-555-0147</span>
      </li>
      <li class="contact-item">
        <svg class="contact-icon" viewBox="0 0 24 24" aria-hidden="true"><path d="M2 6h20v12H2z M3.5 7.5 12 13l8.5-5.5" fill="none" stroke="var(--navy)" stroke-width="0"/><path d="M2 6h20v12H2V6zm2 1.6V16h16V7.6l-8 5.2-8-5.2zM5 7l7 4.5L19 7H5z"/></svg>
        <span>dorian@oakharbor-legal.com</span>
      </li>
      <li class="contact-item">
        <svg class="contact-icon" viewBox="0 0 24 24" aria-hidden="true" fill="none" stroke="var(--navy)" stroke-width="1.8"><circle cx="12" cy="12" r="9"/><ellipse cx="12" cy="12" rx="4" ry="9"/><path d="M3 12h18M4.5 7.5h15M4.5 16.5h15"/></svg>
        <span>www.oakharbor-legal.com</span>
      </li>
    </ul>
  </section>

</main>
</body>
</html>
```